ALL TEXT Social Media Graphics

We are looking for a series of social media graphics for Instagram (new size: 4:5 (1080 x 1350 pixels) ratio that are ALL TEXT. We want the following quotes below on each graphic; one quote per graphic. AND, In very small letters at the bottom of each graphic, add @PaulaWrenLive
The look and feel of these graphics should be complimentary to the color palette attached below; but keep them simple. But the design is up to you; at the end of this document, I provided various samples of all text graphics that I like as examples.
The Quotes are in the attached WORD document
women trying to lose weight

```html
<!DOCTYPE html>
<html lang="en">
<head>
<meta charset="utf-8">
<title>Sunkissed Summer Slimdown – Social Graphics</title>
<link href="https://fonts.googleapis.com/css2?family=Anton&family=Poppins:wght@300;700&family=Roboto:ital,wght@1,700&display=swap" rel="stylesheet">
<style>
  :root{
    --bg:#5e3049;
    --crimson:#a3104f;
    --pink:#f05b9b;
    --ink:#111111;
    --plum:#8a1551;
    --blush:#f3a5c4;
  }
  *{box-sizing:border-box;margin:0;padding:0}
  html,body{width:1200px;height:2894px;overflow:hidden;background:var(--bg)}
  .grid{
    position:relative;width:1200px;height:2894px;
    display:grid;grid-template-columns:417px 417px;column-gap:33px;row-gap:44px;
    padding:58px 0 0 167px;align-content:start;
  }
  .post{
    height:521px;padding:36px 18px 30px 33px;
    display:flex;flex-direction:column;
    background:linear-gradient(to bottom,#fff 0%,#fff 55%,#fbe3ec 78%,var(--blush) 100%);
    box-shadow:0 2px 6px rgba(0,0,0,.18);
  }
  .headline{
    font-family:"Anton",sans-serif;font-weight:400;text-transform:uppercase;
    font-size:43px;line-height:51px;color:var(--crimson);letter-spacing:-.3px;
  }
  .accent{color:var(--pink)}
  .lead{
    font-family:"Roboto",sans-serif;font-style:italic;font-weight:700;
    font-size:25px;line-height:32px;color:var(--ink);margin-top:26px;
  }
  .lead .accent{font-family:"Poppins",sans-serif;font-style:normal;font-weight:700}
  .cta{
    font-family:"Poppins",sans-serif;font-weight:300;font-size:25px;line-height:32px;
    color:var(--plum);margin-top:20px;
  }
  .cta b{font-weight:700}
  .cta .accent{font-weight:700}
  .handle{
    margin-top:auto;font-family:"Poppins",sans-serif;font-style:italic;font-weight:300;
    font-size:15px;color:var(--plum);
  }
</style>
</head>
<body>
<main class="grid">
  <article class="post">
    <h2 class="headline">You can absolutely be down <span class="accent">20–30 pounds</span> by end of summer.</h2>
    <p class="lead">All it takes is the right plan—and you’ve found it.</p>
    <p class="cta">Comment “<b>SUNKISSED</b>” for the Sunkissed Summer Slimdown!</p>
    <p class="handle">@PaulaWrenLive</p>
  </article>
  <article class="post">
    <h2 class="headline">You don’t need another diet—you need a system that works.</h2>
    <p class="lead">Drop <span class="accent">30 pounds</span> with the Sunkissed Summer Slimdown.</p>
    <p class="cta">Comment “<b>Summer</b>” to start now.</p>
    <p class="handle">@PaulaWrenLive</p>
  </article>

  <article class="post">
    <h2 class="headline">This summer ain’t over—and neither are your body goals.</h2>
    <p class="lead">Drop <span class="accent">30 pounds</span> with the Sunkissed Summer Slimdown.</p>
    <p class="cta">Comment “<b>Sunkissed</b>” to get the plan.</p>
    <p class="handle">@PaulaWrenLive</p>
  </article>
  <article class="post">
    <h2 class="headline">If your goal is a tiny waist, flat belly, and <span class="accent">30 pounds</span> down—this is the plan.</h2>
    <p class="cta">Comment “<b>Summer</b>” to join the Sunkissed Summer Slimdown!</p>
    <p class="handle">@PaulaWrenLive</p>
  </article>

  <article class="post">
    <h2 class="headline">There’s still time to drop the <span class="accent">30 pounds</span> and slay this summer.</h2>
    <p class="lead">The <span class="accent">Sunkissed Summer</span> Slimdown has the blueprint.</p>
    <p class="cta">Comment “<b>Sunkissed</b>”!</p>
    <p class="handle">@PaulaWrenLive</p>
  </article>
  <article class="post">
    <h2 class="headline">Snatched waist, flat tummy, <span class="accent">30 pounds</span> lighter</h2>
    <p class="lead" style="margin-top:34px">—that’s what <span class="accent">Sunkissed Summer</span> Slimdown Challenge delivers.</p>
    <p class="cta" style="margin-top:34px">Comment “<b>Sunkissed</b>” to get the plan</p>
    <p class="handle">@PaulaWrenLive</p>
  </article>

  <article class="post">
    <h2 class="headline"><span class="accent">Nothing feels better</span> than seeing that scale drop week after week.</h2>
    <p class="lead">Let’s lose up to <span class="accent">30 pounds</span> this summer—together.</p>
    <p class="cta">Comment “<b>Summer</b>” to join the Sunkissed Summer Slimdown!</p>
    <p class="handle">@PaulaWrenLive</p>
  </article>
  <article class="post">
    <h2 class="headline">Sis, we’re dropping <span class="accent">belly flat</span> and saying goodbye to <span class="accent">stubborn pounds.</span></h2>
    <p class="cta" style="margin-top:40px">Join the <span class="accent">Sunkissed Summer</span> Slimdown—comment “<b>Summer</b>”!</p>
    <p class="handle">@PaulaWrenLive</p>
  </article>

  <article class="post">
    <h2 class="headline"><span class="accent">Don’t wait ’til next summer to get right.</span> The time is now.</h2>
    <p class="lead" style="margin-top:40px">Drop <span class="accent">30 pounds</span> with the Sunkissed Summer Slimdown.</p>
    <p class="cta" style="margin-top:34px">Comment “<b>Summer</b>”</p>
    <p class="handle">@PaulaWrenLive</p>
  </article>
  <article class="post">
    <h2 class="headline">You’ve got <span class="accent">8 weeks</span> and the perfect plan to <span class="accent">drop 30 pounds.</span></h2>
    <p class="lead">Let’s get snatched this summer with the <span class="accent">Sunkissed Summer</span> Slimdown.</p>
    <p class="cta">Comment “<b>Summer</b>”</p>
    <p class="handle">@PaulaWrenLive</p>
  </article>
</main>
</body>
</html>
```